looking to have a web site for the company which provides services in the industrial and commercial sectors such as: electrical, automation control and system integration, construction and maintenance, millwright, equipment assembly repair and installation. I have the domain already brivanholdings.net and logo. Most recent projects fulfilled for the following clients: MarlowKibbleCo, Dunholt University, OKSU, FALSTO, Tazzik, Prairie Grains

Target Market(s)

industrial and commercial sectors in electrical, automation, millwright and fabrication fields

Industry/Entity Type

Industrial

Coding

Coded - Design and coding required

Number of Pages Required

5+ page

Font styles to use
Sans Serif

Colors

Designer to choose colors to be used in the design.

Requirements
Nice to have
• looking to get something not complicated, nicely presented with minimum or no scrolling

```html
<!DOCTYPE html>
<html lang="en">
<head>
<meta charset="utf-8">
<title>Brivan Holdings Ltd</title>
<link href="https://fonts.googleapis.com/css2?family=Roboto:wght@400;500;700&family=Open+Sans:wght@400;600;700&display=swap" rel="stylesheet">
<style>
:root{
  --blue:#1aa3e0;
  --blue-dark:#0f6fa8;
  --ink:#222;
  --text:#666;
  --line:#dcdcdc;
  --footer:#f3f3f3;
  --clients:#4a4d52;
}
*{box-sizing:border-box;margin:0;padding:0}
html,body{width:1200px;height:3098px;overflow:hidden;background:#fff}
body{position:relative;font-family:'Open Sans',sans-serif;color:var(--text)}
.abs{position:absolute}
h1,h2,h3,h4,.nav a,.btn{font-family:'Roboto',sans-serif}
.btn{position:absolute;display:flex;align-items:center;justify-content:center;background:var(--blue);color:#fff;font-size:15px;font-weight:500;text-transform:uppercase;border-radius:4px;text-decoration:none;width:142px;height:42px}

/* header */
.site-header{position:absolute;left:0;top:0;width:1200px;height:87px;background:#fff;box-shadow:0 2px 6px rgba(0,0,0,.15);z-index:3}
.brand{position:absolute;left:99px;top:14px;font-family:'Roboto',sans-serif;font-weight:700;color:#1f5f9e;line-height:1}
.brand .name{font-size:34px;letter-spacing:1px;display:block}
.brand .sub{font-size:15px;letter-spacing:9px;display:block;margin-top:3px}
.nav a{position:absolute;top:36px;font-size:15px;font-weight:500;color:var(--ink);text-decoration:none;text-transform:uppercase}
.nav a.active{color:var(--blue)}

/* hero */
.hero-photo{position:absolute;left:41px;top:87px;width:1118px;height:454px;background:linear-gradient(100deg,#8f9498 0%,#b9bcbe 30%,#cfd3d6 55%,#a6a8a5 75%,#7f8a6f 100%)}
.hero-shadow{position:absolute;left:0;top:430px}
.hero-title{position:absolute;left:0;width:1200px;top:192px;text-align:center;color:#fff;font-size:50px;font-weight:500;text-shadow:0 2px 4px rgba(0,0,0,.3)}
.hero-sub{position:absolute;left:0;width:1200px;top:256px;text-align:center;color:#fff;font-family:'Roboto',sans-serif;font-size:30px;font-weight:500;line-height:45px;text-shadow:0 2px 4px rgba(0,0,0,.3)}
.dots{position:absolute;top:552px;left:575px;display:flex;gap:5px}
.dots span{width:12px;height:12px;border-radius:50%;border:2px solid #fff;background:transparent}
.dots span.on{background:#fff}

/* about */
.about-title{left:99px;top:706px;font-size:30px;font-weight:500;color:var(--ink)}
.about-text{left:99px;top:766px;width:456px;font-size:13.5px;line-height:23px}
.about-text p{margin-bottom:8px}
.about-photo{left:605px;top:669px;width:494px;height:349px;background:linear-gradient(135deg,#8d8f94,#d8d4cc 45%,#e58a2e 60%,#6b6e73);border:3px solid #fff;box-shadow:0 0 0 1px #ddd}

/* services */
.section-title{position:absolute;left:0;width:1200px;text-align:center;font-size:32px;font-weight:500;color:var(--ink)}
.svc-icon{position:absolute;width:100px;height:100px;border-radius:50%;background:var(--blue);display:flex;align-items:center;justify-content:center}
.svc{position:absolute;width:360px}
.svc h4{font-size:17px;font-weight:500;color:var(--ink);text-transform:uppercase;margin-bottom:8px}
.svc p{font-size:13px;line-height:22px}
.svc a{font-family:'Roboto',sans-serif;font-size:13.5px;font-weight:500;color:var(--blue);text-decoration:none}
.svc.right{text-align:right}
.vline{position:absolute;left:599px;width:1px;background:var(--line)}
.hline{position:absolute;top:1291px;height:1px;background:#bbb}

/* band */
.band{left:0;top:1586px;width:1200px;height:359px;background:linear-gradient(90deg,rgba(16,96,160,.95),rgba(30,130,200,.85),rgba(16,96,160,.95))}
.band h2{position:absolute;left:0;width:1200px;top:60px;text-align:center;color:#fff;font-size:32px;font-weight:500;line-height:46px;text-transform:uppercase}
.band p{position:absolute;left:200px;width:800px;top:166px;text-align:center;color:#fff;font-size:14px;font-weight:600;line-height:27px}

/* features */
.feat-photo{left:99px;top:2009px;width:585px;height:376px;background:linear-gradient(120deg,#7a7a78,#b0aaa0 40%,#8a6f58 70%,#555);box-shadow:0 0 0 1px #ccc}
.feat-box{left:128px;top:2034px;width:264px;height:320px;background:var(--blue);padding:10px}
.feat-box .inner{border:2px solid #fff;height:100%;padding:26px 26px;color:#fff}
.feat-box h3{font-size:20px;font-weight:500;margin-bottom:16px}
.feat-box p{font-size:12.5px;line-height:21px;margin-bottom:12px}
.feat-list{left:684px;top:2042px;width:419px;border:1px solid #ccc;background:#fff}
.feat-item{position:relative;height:103px;border-bottom:1px solid #ccc;padding:14px 0 0 88px}
.feat-item:last-child{border-bottom:none}
.feat-item.on{border-right:5px solid var(--blue-dark)}
.feat-item svg{position:absolute;left:38px;top:28px}
.feat-item h4{font-size:22px;font-weight:500;color:var(--ink);text-transform:uppercase;margin-bottom:4px}
.feat-item p{font-size:14px;line-height:22px;color:#777}

/* clients */
.clients{left:0;top:2437px;width:1200px;height:309px;background:linear-gradient(180deg,#55585d,#3f4247)}
.clients .section-title{top:64px;color:#fff}
.client{position:absolute;top:134px;width:217px;height:97px;background:#fff;border-radius:6px;display:flex;align-items:center;justify-content:center;gap:10px;font-family:'Roboto',sans-serif;font-weight:700;font-size:28px;color:#1e3b70}
.client i{width:14px;height:14px;background:#1e3b70;display:inline-block}
.arrow{position:absolute;top:165px}

/* footer */
.site-footer{left:0;top:2746px;width:1200px;height:352px;background:var(--footer)}
.foot-brand{left:99px;top:118px}
.foot-col{position:absolute;top:60px}
.foot-col h4{font-size:18px;font-weight:500;color:var(--ink);text-transform:uppercase;margin-bottom:20px}
.foot-col li{list-style:none;font-size:13.5px;line-height:25px;color:#555}
.contact li{position:relative;padding-left:22px;line-height:22px;margin-bottom:8px}
.contact svg{position:absolute;left:0;top:5px}
.social li{display:flex;align-items:center;gap:10px;line-height:34px}
.social i{width:12px;height:12px;display:inline-block}
.foot-rule{position:absolute;left:99px;top:283px;width:1004px;height:1px;background:#ccc}
.copy{position:absolute;left:0;top:306px;width:1200px;text-align:center;font-size:13px;color:#555}
</style>
</head>
<body>

<header class="site-header">
  <div class="brand"><span class="name">BRIVAN</span><span class="sub">HOLDINGS</span></div>
  <nav class="nav">
    <a class="active" style="left:475px" href="#">Home</a>
    <a style="left:557px" href="#">About Us</a>
    <a style="left:669px" href="#">Services</a>
    <a style="left:778px" href="#">Clients</a>
    <a style="left:878px" href="#">Blog</a>
    <a style="left:954px" href="#">Contact Us</a>
    <svg class="abs" style="left:1086px;top:37px" width="16" height="16" viewBox="0 0 16 16"><circle cx="6.5" cy="6.5" r="5" fill="none" stroke="#222" stroke-width="2"/><path d="M10 10l5 5" stroke="#222" stroke-width="2.4"/></svg>
  </nav>
</header>

<section class="hero">
  <svg class="hero-shadow" width="1200" height="180" viewBox="0 0 1200 180">
    <defs><linearGradient id="sh" x1="0" y1="0" x2="0" y2="1"><stop offset="0" stop-color="#8a8a8a"/><stop offset="1" stop-color="#d8d8d8" stop-opacity=".3"/></linearGradient></defs>
    <polygon points="0,0 41,0 41,111 1159,111 1159,0 1200,0 1200,20 600,173 0,20" fill="#b0b0b0"/>
    <polygon points="41,111 1159,111 600,173" fill="url(#sh)"/>
  </svg>
  <div class="hero-photo" role="img" aria-label="Industrial grain silos and loading facility beside a rail line"></div>
  <h1 class="hero-title">BRIVAN HOLDINGS LTD</h1>
  <p class="hero-sub">Nam Libero Tempore, Cum Soluta Nobis Est<br>Eligendi Optio Cumque Nihil</p>
  <a class="btn" style="left:529px;top:363px" href="#">Read More</a>
  <div class="dots"><span class="on"></span><span></span><span></span></div>
</section>

<section class="about">
  <h2 class="abs about-title">ABOUT US</h2>
  <div class="abs about-text">
    <p>At vero eos et accusamus et iusto odio dignissimos ducimus qui bla nditiis praesentium voluptatum deleniti atque corrupti quos dolores et quas molestias excepturi sint occaecati cupiditate.</p>
    <p>Provident, similique sunt in culpa qui officia deserunt mollitia animi, id est laborum et dolorum fuga. Et harum quidem rerum facilis est et expedita distinctio.</p>
  </div>
  <a class="btn" style="left:99px;top:931px" href="#">Read More</a>
  <div class="abs about-photo" role="img" aria-label="Three warehouse workers in high-visibility vests"></div>
</section>

<section class="services">
  <h2 class="section-title" style="top:1082px">OUR SERVICES</h2>

  <div class="svc-icon" style="left:123px;top:1160px"><svg width="46" height="46" viewBox="0 0 46 46"><path d="M27 4L11 26h11l-4 16 17-23H24z" fill="none" stroke="#fff" stroke-width="2.4" stroke-linejoin="round"/></svg></div>
  <div class="svc" style="left:250px;top:1162px"><h4>Electrical</h4><p>At vero eos et accusamus et iusto odio dignissimos ducimus qui blanditiis praesentium voluptatum..</p><a href="#">READ MORE ⟶</a></div>

  <div class="svc right" style="left:588px;top:1162px"><h4>Automation Control</h4><p>At vero eos et accusamus et iusto odio dignissimos ducimus qui blanditiis praesentium voluptatum..</p><a href="#">READ MORE ⟶</a></div>
  <div class="svc-icon" style="left:972px;top:1160px"><svg width="50" height="50" viewBox="0 0 50 50" fill="none" stroke="#fff" stroke-width="2.2"><rect x="7" y="10" width="32" height="26" rx="6"/><circle cx="17" cy="21" r="3"/><circle cx="29" cy="21" r="3"/><circle cx="36" cy="35" r="7" fill="#1aa3e0"/><path d="M33 35l2 2 4-4"/></svg></div>

  <div class="svc-icon" style="left:123px;top:1315px"><svg width="50" height="50" viewBox="0 0 50 50" fill="none" stroke="#fff" stroke-width="2.2"><rect x="16" y="16" width="18" height="18" rx="2"/><path d="M16 16L7 7M34 16l9-9M16 34l-9 9M34 34l9 9M5 7h6M5 7v6M45 7h-6M45 7v6M5 43h6M5 43v-6M45 43h-6M45 43v-6"/></svg></div>
  <div class="svc" style="left:250px;top:1317px"><h4>System Integration</h4><p>At vero eos et accusamus et iusto odio dignissimos ducimus qui blanditiis praesentium voluptatum..</p><a href="#">READ MORE ⟶</a></div>

  <div class="svc right" style="left:588px;top:1317px"><h4>Equipment Installation</h4><p>At vero eos et accusamus et iusto odio dignissimos ducimus qui blanditiis praesentium voluptatum..</p><a href="#">READ MORE ⟶</a></div>
  <div class="svc-icon" style="left:972px;top:1315px"><svg width="50" height="50" viewBox="0 0 50 50" fill="none" stroke="#fff" stroke-width="2.2"><rect x="8" y="12" width="22" height="28" rx="2"/><rect x="13" y="17" width="12" height="6"/><circle cx="19" cy="32" r="4"/><rect x="28" y="24" width="16" height="16" rx="2"/><circle cx="36" cy="32" r="3"/></svg></div>

  <div class="vline" style="top:1152px;height:104px"></div>
  <div class="vline" style="top:1307px;height:118px"></div>
  <div class="hline" style="left:145px;width:423px"></div>
  <div class="hline" style="left:632px;width:423px"></div>

  <a class="btn" style="left:529px;top:1474px" href="#">View All</a>
</section>

<section class="abs band" role="img" aria-label="Blue-tinted industrial plant interior behind the text">
  <h2>We provide services in the industrial<br>and commercial sectors</h2>
  <p>At Vero Eos Et Accusamus Et Iusto Odio Dignissimos Ducimus Qui Blanditiis Praesentium Voluptatum Deleniti Atque Corrupti Quos Dolores Et Quas Molestias Excepturi Sint Occaecati Cupiditate Non Provident</p>
  <a class="btn" style="left:529px;top:242px" href="#">Read More</a>
</section>

<section class="features">
  <div class="abs feat-photo" role="img" aria-label="Factory workshop with machinery and conveyor frames"></div>
  <div class="abs feat-box"><div class="inner">
    <h3>Modern Hardware</h3>
    <p>Sed ut perspiciatis unde omnis iste natus error sit voluptatem accusantium doloremque la udantium, totam rem.</p>
    <p>Nemo enim ipsam voluptatem quia voluptas sit aspernatur aut odit aut fugit.</p>
  </div></div>
  <div class="abs feat-list">
    <div class="feat-item on">
      <svg width="40" height="40" viewBox="0 0 40 40" fill="none" stroke="#1aa3e0" stroke-width="1.8"><path d="M20 8l4 8 9 1-7 6 2 9-8-5-8 5 2-9-7-6 9-1z"/><path d="M6 4l1 3 3 .5-2 2 .5 3L6 11 3.5 12.5 4 9.5l-2-2 3-.5zM34 4l1 3 3 .5-2 2 .5 3-2.5-1.5-2.5 1.5.5-3-2-2 3-.5z"/></svg>
      <h4>Modern Hardware</h4><p>Sed Ut Perspiciatis Unde Omnis Iste<br>Natus Error Sit Voluptatem Accusantium</p>
    </div>
    <div class="feat-item">
      <svg width="40" height="40" viewBox="0 0 40 40" fill="none" stroke="#1aa3e0" stroke-width="1.8"><path d="M20 4l14 5v10c0 9-6 15-14 18C12 34 6 28 6 19V9z"/><path d="M13 20h5l3-4 4 1v7h-9z"/></svg>
      <h4>Customer Satisfaction</h4><p>Sed Ut Perspiciatis Unde Omnis Iste<br>Natus Error Sit Voluptatem Accusantium</p>
    </div>
    <div class="feat-item">
      <svg width="40" height="40" viewBox="0 0 40 40" fill="none" stroke="#1aa3e0" stroke-width="1.8"><rect x="5" y="12" width="30" height="22" rx="2"/><path d="M15 12V8h10v4M5 21h30M18 21v3h4v-3"/></svg>
      <h4>Professional Staffs</h4><p>Sed Ut Perspiciatis Unde Omnis Iste<br>Natus Error Sit Voluptatem Accusantium</p>
    </div>
  </div>
</section>

<section class="abs clients">
  <h2 class="section-title">OUR CLIENTS</h2>
  <svg class="arrow" style="left:44px" width="20" height="30" viewBox="0 0 20 30"><path d="M15 4L5 15l10 11" fill="none" stroke="#fff" stroke-width="3"/></svg>
  <div class="client" style="left:99px"><i></i>FALSTO</div>
  <div class="client" style="left:361px;font-size:25px">Dunholt University</div>
  <div class="client" style="left:624px">Tazzik</div>
  <div class="client" style="left:886px"><i></i>OKSU</div>
  <svg class="arrow" style="left:1138px" width="20" height="30" viewBox="0 0 20 30"><path d="M5 4l10 11L5 26" fill="none" stroke="#fff" stroke-width="3"/></svg>
</section>

<footer class="abs site-footer">
  <div class="abs foot-brand brand" style="left:99px;top:118px"><span class="name">BRIVAN</span><span class="sub">HOLDINGS</span></div>
  <div class="foot-col" style="left:442px">
    <h4>Quick Links</h4>
    <ul><li>Home</li><li>About Us</li><li>Services</li><li>Clients</li><li>Blog</li><li>Contact Us</li></ul>
  </div>
  <div class="foot-col contact" style="left:679px">
    <h4>Contact Us</h4>
    <ul>
      <li><svg width="12" height="14" viewBox="0 0 12 14"><path d="M6 0a5 5 0 015 5c0 4-5 9-5 9S1 9 1 5a5 5 0 015-5z" fill="#1aa3e0"/><circle cx="6" cy="5" r="2" fill="#fff"/></svg>Lorem Ipsum<br>Contray To Belief</li>
      <li><svg width="13" height="10" viewBox="0 0 13 10"><rect width="13" height="10" rx="1" fill="#1aa3e0"/><path d="M1 1l5.5 4.5L12 1" stroke="#fff" fill="none"/></svg>info@brivanholdings.net</li>
      <li><svg width="12" height="12" viewBox="0 0 12 12"><path d="M2 0h3l1 3-2 1.5a7 7 0 003.5 3.5L9 6l3 1v3c0 1-1 2-2 2C4.5 12 0 7.5 0 2 0 1 1 0 2 0z" fill="#1aa3e0"/></svg>+1 888 888 8888</li>
      <li><svg width="13" height="12" viewBox="0 0 13 12"><rect x="0" y="3" width="13" height="9" rx="1" fill="#1aa3e0"/><rect x="3" y="0" width="7" height="4" fill="#1aa3e0"/><rect x="3" y="6" width="7" height="3" fill="#fff"/></svg>888 888 8888</li>
    </ul>
  </div>
  <div class="foot-col social" style="left:981px">
    <h4>Social Links</h4>
    <ul>
      <li style="color:#3b5998"><i style="background:#3b5998"></i>Friendlane</li>
      <li style="color:#d23b2e"><i style="background:#d23b2e"></i>Searchly</li>
      <li style="color:#f08a1c"><i style="background:#f08a1c"></i>Worknet</li>
      <li style="color:#1aa3e0"><i style="background:#1aa3e0"></i>Chirpline</li>
    </ul>
  </div>
  <div class="foot-rule"></div>
  <p class="copy">Copyright © 2017 Brivan Holdings Ltd. All Rights Reserved.</p>
</footer>

</body>
</html>
```